ZRD Roofing Billboard Design

Looking for a fresh new billboard design with my new headshot photo and using some info from my previous billboard and maybe website for design/content inspiration. My website is https://zrdroofing.com/

Also attached are my logo and current lawn sign design. I am looking for something simple, clean and modern. The landing page website should be 3816tops.com like my previous billboard has.

```html
<!DOCTYPE html>
<html lang="en">
<head>
<meta charset="utf-8">
<title>ZRD Roofing Billboard</title>
<link rel="stylesheet" href="https://fonts.googleapis.com/css2?family=Anton&family=Archivo+Black&family=Montserrat:wght@700&display=swap">
<style>
  :root {
    --page-bg: #dcdcdc;
    --navy: #23406d;
    --navy-deep: #16294a;
    --green: #8fa61e;
    --green-bright: #9cb51f;
    --white: #ffffff;
    --photo-light: #8ea4c8;
    --photo-dark: #2d4a78;
  }
  html, body {
    margin: 0;
    padding: 0;
    width: 1021px;
    height: 1200px;
    overflow: hidden;
    background: var(--page-bg);
  }
  .billboard {
    position: absolute;
    left: 30px;
    top: 460px;
    width: 961px;
    height: 281px;
    display: block;
  }
  .headline { font-family: "Anton", "Oswald", sans-serif; fill: var(--white); }
  .heavy { font-family: "Archivo Black", "Arial Black", sans-serif; }
  .brand-name { font-family: "Montserrat", sans-serif; font-weight: 700; fill: var(--navy); }
</style>
</head>
<body>
<svg class="billboard" viewBox="0 0 1397 408" xmlns="http://www.w3.org/2000/svg">
  <defs>
    <linearGradient id="photoTone" x1="0" y1="0" x2="1" y2="1">
      <stop offset="0" stop-color="var(--photo-dark)"/>
      <stop offset="0.55" stop-color="var(--photo-light)"/>
      <stop offset="1" stop-color="var(--photo-dark)"/>
    </linearGradient>
  </defs>

  <!-- main field -->
  <rect class="field" x="0" y="0" width="1397" height="408" fill="var(--navy)"/>

  <!-- portrait over rooftops -->
  <rect class="portrait" x="975" y="0" width="422" height="408" fill="url(#photoTone)" role="img" aria-label="Headshot of the company owner in a light blue shirt in front of aerial view of house roofs"/>

  <!-- brand panel -->
  <polygon class="brand-panel" points="0,0 338,0 472,328 0,328" fill="var(--white)"/>
  <circle class="brand-dot" cx="225" cy="168" r="70" fill="var(--green)"/>
  <text class="brand-name" x="225" y="296" font-size="32" text-anchor="middle" textLength="362" lengthAdjust="spacingAndGlyphs">ZRD Roofing LLC</text>

  <!-- headline -->
  <text class="headline" x="498" y="116" font-size="112" textLength="494" lengthAdjust="spacingAndGlyphs">FULL ROOF</text>
  <text class="headline" x="498" y="191" font-size="74" textLength="490" lengthAdjust="spacingAndGlyphs">REPLACEMENT</text>

  <!-- price pill -->
  <rect class="price-pill" x="492" y="233" width="486" height="68" rx="22" fill="var(--navy-deep)"/>
  <rect class="price-tag" x="718" y="233" width="260" height="68" rx="26" fill="var(--green-bright)"/>
  <text class="heavy" x="514" y="280" font-size="30" fill="var(--white)" textLength="190" lengthAdjust="spacingAndGlyphs">Starting @</text>
  <text class="heavy" x="740" y="289" font-size="24" fill="var(--white)">$</text>
  <text class="heavy" x="758" y="290" font-size="52" fill="var(--white)" textLength="200" lengthAdjust="spacingAndGlyphs">7,499</text>

  <!-- contact band -->
  <polygon class="phone-band" points="0,330 472,330 440,408 0,408" fill="var(--navy-deep)"/>
  <polygon class="web-band" points="472,328 995,328 975,408 432,408" fill="var(--green)"/>
  <text class="heavy" x="45" y="386" font-size="38" fill="var(--white)" textLength="372" lengthAdjust="spacingAndGlyphs">(555) 271-0386</text>
  <text class="heavy" x="490" y="391" font-size="50" fill="var(--white)" textLength="460" lengthAdjust="spacingAndGlyphs">3816TOPS.COM</text>
</svg>
</body>
</html>
```